Eine Willkommenseite (Startseite) für WohnFokus
Zielgruppe
Die Zielgruppe sind Kunden (Business, Privat und öffentliche Einrichtungen) die Immobilien über das Wohnfokus-Portal kostenlos suchen oder inserieren möchten. Quasi alle Besucher, die Immobilen über WohnFokus ohne Inseratkosten verkaufen, kaufen, vermieten, mieten und versteigern wollen.
Aufgabenstellung
Die Willkommenseite für WohnFokus.
Problemstellung: WohnFokus ist seit ca. 3 Monaten erfolgreich online. Die Immobilen Webseite von WohnFokus ist schlicht, dezent sowie funktionell aufgebaut. WohnFokus fehlt eine ansprechende Willkommenseite. Die Willkommenseite sollte emotional ansprechend und dem/der BesucherIn ein "Wow" entlocken sowie zu einem weiteren Surfen auf WohnFokus einladen.

```html
<!DOCTYPE html>
<html lang="de">
<head>
<meta charset="utf-8">
<title>WohnFokus – Willkommen</title>
<link href="https://fonts.googleapis.com/css2?family=Arimo:wght@400;700&family=Noto+Sans:wght@400;700&display=swap" rel="stylesheet">
<style>
:root{
  --page-bg:#c8d4e6;
  --page-band:#e4eaf3;
  --panel-top:#a9bfe0;
  --panel-mid:#7c9dd0;
  --panel-low:#6a8dc6;
  --ink:#0d0d12;
  --frame:#1a1a24;
  --logo:#0f0f14;
  --link-strip:#c98a7a;
  --tick-light:#c9ef7a;
  --tick-dark:#5fa818;
  --btn-light:#a6e04a;
  --btn-dark:#4e9a12;
  --arrow:#f0a028;
  --ad-bg:#ffffff;
  --ad-border:#c5cbd6;
  --ad-link:#5b8fd2;
  --photo-warm:#c79266;
  --photo-deep:#8a5a36;
}
*{box-sizing:border-box;margin:0;padding:0}
html,body{width:1200px;height:614px;overflow:hidden}
body{
  position:relative;
  font-family:"Noto Sans",sans-serif;
  color:var(--ink);
  background:linear-gradient(180deg,var(--page-bg) 0,var(--page-bg) 490px,var(--page-band) 502px,var(--page-band) 562px,#a9b8cf 572px,var(--page-bg) 580px);
}
.welcome-panel{
  position:absolute;left:205px;top:13px;width:792px;height:591px;
  border:2px solid var(--frame);overflow:hidden;
  background:
    radial-gradient(ellipse 360px 110px at 380px 40px,rgba(255,255,255,.85),rgba(255,255,255,0) 100%),
    linear-gradient(180deg,var(--panel-top) 0,var(--panel-mid) 220px,var(--panel-low) 591px);
}
.brand{
  position:absolute;left:112px;top:24px;
  font-family:"Arimo",sans-serif;font-weight:700;font-size:45px;letter-spacing:.5px;color:var(--logo);
  display:flex;align-items:center;gap:14px;
}
.brand-mark{width:16px;height:16px;background:var(--logo)}
.meta-nav{
  position:absolute;right:0;top:2px;width:78px;height:64px;
  background:linear-gradient(90deg,rgba(201,138,122,0),var(--link-strip) 40%);
  display:flex;flex-direction:column;align-items:flex-end;padding-right:8px;
}
.meta-nav a{color:#fff;font-size:9.5px;letter-spacing:1px;text-decoration:none;line-height:16px}
.section-title{position:absolute;left:40px;top:121px;font-size:15px;font-weight:700}
.gallery{position:absolute;left:39px;width:204px;height:120px;border:2px solid var(--frame)}
.gallery p,.team-photo p{font-size:10px;letter-spacing:.8px;line-height:12px}
.gallery p{padding:40px 0 0 25px}
.gallery-arrow{position:absolute;top:56px;width:0;height:0;border-top:6px solid transparent;border-bottom:6px solid transparent}
.gallery-arrow.prev{left:-13px;border-right:6px solid var(--frame)}
.gallery-arrow.next{right:-15px;border-left:6px solid var(--frame)}
.divider{position:absolute;left:285px;top:123px;width:2px;height:295px;background:rgba(110,110,120,.55)}
.benefits{position:absolute;left:329px;top:117px;list-style:none}
.benefits li{display:flex;align-items:center;gap:11px;height:57px;font-size:24px;font-family:"Arimo",sans-serif}
.benefits svg{width:40px;height:40px}
.team-photo{position:absolute;left:325px;top:305px;width:204px;height:120px;border:2px solid var(--frame)}
.team-photo p{padding:12px 0 0 10px}
.cta{
  position:absolute;left:635px;top:304px;width:128px;height:41px;border-radius:5px;
  background:linear-gradient(180deg,var(--btn-light),var(--btn-dark));
  box-shadow:0 2px 3px rgba(0,0,0,.35);
  display:flex;align-items:center;gap:12px;padding-left:10px;
  font-family:"Arimo",sans-serif;font-weight:700;font-size:17px;color:#2b3d12;text-decoration:none;
}
.slogan-band{
  position:absolute;left:0;top:482px;width:650px;height:72px;
  background:linear-gradient(90deg,rgba(245,236,232,.95) 0,rgba(240,228,228,.85) 55%,rgba(240,228,228,0) 100%);
}
.slogan-band p{position:absolute;left:13px;top:26px;font-size:20px;font-weight:700}
.hero-visual{
  position:absolute;left:470px;top:366px;width:322px;height:212px;
  background:radial-gradient(ellipse 120px 90px at 180px 80px,var(--photo-warm),rgba(199,146,102,0) 100%),
             radial-gradient(ellipse 200px 60px at 230px 170px,var(--photo-deep),rgba(138,90,54,0) 100%);
}
.social{position:absolute;left:16px;top:565px;display:flex;gap:8px}
.social span{width:15px;height:15px;border-radius:2px;background:#eef2f8;border:1px solid #9fb3d3}
.ads{position:absolute;left:1001px;top:13px;display:flex;flex-direction:column;gap:5px}
.ad{
  width:131px;height:132px;background:var(--ad-bg);border:1px solid var(--ad-border);
  text-align:center;font-family:"Arimo",sans-serif;
}
.ad-brand{margin-top:46px;font-weight:700;font-size:13px;color:var(--logo)}
.ad-copy{margin-top:12px;font-size:14px;line-height:16px}
.ad-link{font-weight:700;font-size:14px;color:var(--ad-link);padding-left:14px}
</style>
</head>
<body>
<main class="welcome-panel">
  <div class="brand"><span class="brand-mark"></span>WOHNFOKUS</div>
  <nav class="meta-nav"><a href="#">Login</a><a href="#">Registrieren</a><a href="#">AGB</a><a href="#">Impressum</a></nav>

  <h2 class="section-title">Neue Immobilien:</h2>
  <div class="gallery" style="top:148px"><span class="gallery-arrow prev"></span><p>neue immobilien 255x150px<br><br>evtl. dynamische javascript<br>Bildergalerie?</p><span class="gallery-arrow next"></span></div>
  <div class="gallery" style="top:305px"><span class="gallery-arrow prev"></span><span class="gallery-arrow next"></span></div>

  <div class="divider"></div>

  <ul class="benefits">
    <li><svg viewBox="0 0 40 40"><defs><radialGradient id="tk" cx="40%" cy="30%" r="70%"><stop offset="0" stop-color="#eaffb8"/><stop offset=".5" stop-color="#9fd848"/><stop offset="1" stop-color="#4f9a12"/></radialGradient></defs><circle cx="20" cy="20" r="18.5" fill="url(#tk)" stroke="#dfe8c8" stroke-width="2"/><path d="M11 21l6 6 12-13" fill="none" stroke="#fff" stroke-width="4.5" stroke-linecap="round" stroke-linejoin="round"/></svg>Immobilien in ganz Europa</li>
    <li><svg viewBox="0 0 40 40"><circle cx="20" cy="20" r="18.5" fill="url(#tk)" stroke="#dfe8c8" stroke-width="2"/><path d="M11 21l6 6 12-13" fill="none" stroke="#fff" stroke-width="4.5" stroke-linecap="round" stroke-linejoin="round"/></svg>komfortabel &amp; verlässlich</li>
    <li><svg viewBox="0 0 40 40"><circle cx="20" cy="20" r="18.5" fill="url(#tk)" stroke="#dfe8c8" stroke-width="2"/><path d="M11 21l6 6 12-13" fill="none" stroke="#fff" stroke-width="4.5" stroke-linecap="round" stroke-linejoin="round"/></svg>garantiert kostenlos</li>
  </ul>

  <div class="team-photo"><p>evtl. ein Foto vom Team,<br>Hauptsitz, Büro o.ä.</p></div>

  <a class="cta" href="#"><svg width="44" height="22" viewBox="0 0 44 22"><path d="M1 6h26V1l16 10-16 10v-5H1z" fill="var(--arrow)" stroke="#8a5a10" stroke-width="1"/></svg>WEITER</a>

  <div class="slogan-band"><p>Vielleicht das Plätzchen für einen Slogan?</p></div>
  <div class="hero-visual" role="img" aria-label="Foto: offene Hand, die ein Holzhaus im Rohbau hält"></div>

  <div class="social" aria-label="Soziale Netzwerke"><span></span><span></span><span></span><span></span><span></span></div>
</main>

<aside class="ads">
  <div class="ad"><div class="ad-brand">WOHNFOKUS</div><div class="ad-copy">Ihre Werbung ?</div><div class="ad-link">Hier klicken ...</div></div>
  <div class="ad"><div class="ad-brand">WOHNFOKUS</div><div class="ad-copy">Ihre Werbung ?</div><div class="ad-link">Hier klicken ...</div></div>
  <div class="ad"><div class="ad-brand">WOHNFOKUS</div><div class="ad-copy">Ihre Werbung ?</div><div class="ad-link">Hier klicken ...</div></div>
  <div class="ad"><div class="ad-brand">WOHNFOKUS</div><div class="ad-copy">Ihre Werbung ?</div><div class="ad-link">Hier klicken ...</div></div>
</aside>
</body>
</html>
```